Torvenu Business Card Design Project

We need a business card design for torvenu.com a company based in Berlin, Germany.

?Torvenu is marketplace that enables people all over the world to monetize and exchange their individual knowledge and language skills through interactive video sessions. User are matched by their interests.

On Torvenu everybody can be student or teacher (seller or buyer).

We would love to see designs that use or main color blue and green. The design should communicate what Torvenu enables - see my notice above.

Looking so forward to your designs
Cheers from Berlin,
Konrad

Target Market(s)

globally

Industry/Entity Type

Teacher

Requirements
Must have
• Konrad Wielert
CEO
Torvenu.com

Torvenu e-Services GmbH
Lindgrubweg 27
10117 Berlin

Fon: +49 30 481 906 27 14
Mobile: 49 171 57 04 91 3
E-Mail: k.wielert@torvenu.com
Web: www.torvenu.com

```html
<!DOCTYPE html>
<html lang="en">
<head>
<meta charset="utf-8">
<title>Torvenu Business Card</title>
<link href="https://fonts.googleapis.com/css2?family=Quicksand:wght@400;500;600&display=swap" rel="stylesheet">
<style>
  :root {
    --stage: #d9d9d9;
    --card-front: #ededed;
    --card-back: #f3f3f3;
    --brand-blue: #0e9ad7;
    --brand-green: #9cc20e;
    --ink-grey: #5a5a5a;
    --ink-light: #7a7a7a;
  }
  * { margin: 0; padding: 0; box-sizing: border-box; }
  html, body { width: 1200px; height: 880px; overflow: hidden; }
  body {
    background: var(--stage);
    font-family: "Quicksand", "Helvetica Neue", Arial, sans-serif;
    display: flex;
    align-items: center;
    justify-content: center;
    gap: 40px;
  }
  .card {
    position: relative;
    width: 540px;
    height: 340px;
    border-radius: 28px;
    overflow: hidden;
    box-shadow: 0 8px 24px rgba(0,0,0,0.15);
  }
  .card-front { background: var(--card-front); }
  .card-back { background: var(--card-back); }
  .card-shape { position: absolute; inset: 0; width: 100%; height: 100%; }

  .brand-name {
    display: flex;
    align-items: center;
    gap: 10px;
    color: var(--ink-grey);
    font-weight: 500;
    letter-spacing: 0.5px;
  }
  .brand-square { background: var(--brand-blue); display: block; }

  .front-brand { position: absolute; left: 36px; top: 34px; font-size: 30px; }
  .front-brand .brand-square { width: 20px; height: 20px; }

  .holder { position: absolute; left: 36px; top: 110px; }
  .holder-name {
    color: var(--brand-blue);
    font-size: 14px;
    font-weight: 600;
    letter-spacing: 1px;
    text-transform: uppercase;
  }
  .holder-role { color: var(--ink-light); font-size: 12px; margin-top: 2px; }

  .company { position: absolute; left: 36px; top: 178px; font-size: 12px; line-height: 19px; color: var(--ink-light); }
  .company-name { color: var(--brand-green); font-weight: 600; }

  .contacts { position: absolute; left: 300px; top: 150px; font-size: 12px; line-height: 20px; color: var(--ink-grey); list-style: none; }
  .contacts .label { color: var(--brand-blue); font-weight: 600; display: inline-block; width: 18px; }

  .back-brand {
    position: absolute;
    left: 150px;
    top: 180px;
    font-size: 62px;
  }
  .back-brand .brand-square { width: 38px; height: 38px; }
  .back-web {
    position: absolute;
    left: 200px;
    top: 262px;
    font-size: 13px;
    letter-spacing: 6px;
    color: var(--ink-light);
  }
</style>
</head>
<body>
  <section class="card card-front" aria-label="Card front">
    <svg class="card-shape" viewBox="0 0 540 340" aria-hidden="true">
      <path d="M402 262 H540 V340 H382 V282 Q382 262 402 262 Z" fill="var(--brand-blue)"/>
      <path d="M396 262 L368 240 L426 262 Z" fill="var(--brand-blue)"/>
    </svg>
    <div class="brand-name front-brand"><span class="brand-square"></span>torvenu</div>
    <div class="holder">
      <p class="holder-name">Konrad Wielert</p>
      <p class="holder-role">CEO</p>
    </div>
    <div class="company">
      <p class="company-name">Torvenu e-Services GmbH</p>
      <p>Lindgrubweg 27</p>
      <p>10117 Berlin</p>
    </div>
    <ul class="contacts">
      <li><span class="label">p:</span>+49 30 481 906 27 14</li>
      <li><span class="label">m:</span>49 171 57 04 91 3</li>
      <li><span class="label">e:</span>k.wielert@torvenu.com</li>
      <li><span class="label">w:</span>www.torvenu.com</li>
    </ul>
  </section>

  <section class="card card-back" aria-label="Card back">
    <svg class="card-shape" viewBox="0 0 540 340" aria-hidden="true">
      <path d="M0 0 H230 V140 H128 L102 172 L100 140 H0 Z" fill="var(--brand-green)"/>
      <circle cx="150" cy="0" r="22" fill="var(--stage)"/>
    </svg>
    <div class="brand-name back-brand"><span class="brand-square"></span>torvenu</div>
    <p class="back-web">www.torvenu.com</p>
  </section>
</body>
</html>
```